Business Card- Occupational Therapist

I need business cards for Tallowood KinderMove, I am an Occupational Therapist offering child centred play therapy.
I am a sole private practitioner offering play therapy services to families in rural Great Southern region of WA, my mission statement is "helping rural children and communities thrive"
This is a new business so I am needing to promote the value of child centred play therapy within the community, and my referrers (target audience) will be: rural GPs (doctors), child health nurse, schools, disability providers, child protection workers etc) but also the families of young children in rural areas.
Target Market(s)
Families of children
Referrers (Doctors, child health nurse, schools, disability providers, child protection workers)
Industry/Entity Type
Mental Health
Contact Information for Business Card
Mira Toveland
Occupational Therapist
Phone: 0487 552 019
Email: mira@tkmove.com.au
PO Box 71 | MARROWBANK WA 6401
Requirements
Must have
- Include Tallowood KinderMove logo and my contact details.
Include my credentials as an Occupational Therapist and Child Centred Play Therapist
Nice to have
- "Play is a child's language and toys are their words" Delbert Quorin

```html
<!DOCTYPE html>
<html lang="en">
<head>
<meta charset="utf-8">
<title>Tallowood KinderMove – Business Card</title>
<link rel="stylesheet" href="https://fonts.googleapis.com/css2?family=Didact+Gothic&family=Poppins:wght@600&display=swap">
<style>
  :root {
    --plum: #6a2162;
    --plum-soft: #b48bb0;
    --leaf: #22a74a;
    --ink: #2b2b2b;
    --grey-text: #555555;
    --paper: #ffffff;
    --backdrop: #d9d9d7;
  }
  * { margin: 0; padding: 0; box-sizing: border-box; }
  html, body {
    width: 1200px; height: 801px; overflow: hidden;
    background: var(--backdrop);
    font-family: "Didact Gothic", "Century Gothic", sans-serif;
  }
  .stage { position: relative; width: 1200px; height: 801px; }
  .card {
    position: absolute; width: 540px; height: 330px; overflow: hidden;
    box-shadow: 0 6px 18px rgba(0,0,0,0.18);
  }
  /* Front */
  .card-front { left: 40px; top: 235px; background: var(--paper); }
  .front-swoop { position: absolute; inset: 0; width: 540px; height: 330px; }
  .brand {
    position: absolute; left: 40px; top: 60px; width: 175px;
    display: flex; flex-direction: column; align-items: center; gap: 14px;
  }
  .brand-name {
    font-size: 26px; line-height: 1.15; color: var(--ink); text-align: center;
  }
  .brand-dot { width: 56px; height: 56px; border-radius: 50%; background: var(--leaf); }
  .divider {
    position: absolute; left: 232px; top: 40px; width: 1px; height: 145px;
    background: var(--plum-soft);
  }
  .details { position: absolute; left: 252px; top: 34px; color: var(--grey-text); }
  .person-name {
    font-family: "Poppins", sans-serif; font-weight: 600;
    font-size: 19px; color: var(--plum); line-height: 1.1;
  }
  .credential { font-size: 12.5px; line-height: 1.35; }
  .address { font-size: 12.5px; line-height: 1.35; margin-top: 12px; }
  .contact-list { list-style: none; margin-top: 10px; font-size: 12.5px; line-height: 1.45; }
  .contact-list li { display: flex; align-items: center; gap: 6px; }
  .contact-list svg { width: 10px; height: 10px; fill: var(--leaf); flex: none; }
  /* Back */
  .card-back { left: 620px; top: 235px; background: var(--plum); }
  .back-mark {
    position: absolute; left: 40px; top: 70px; width: 190px;
    display: flex; flex-direction: column; align-items: center; gap: 16px;
  }
  .back-mark .brand-dot { width: 120px; height: 120px; }
  .back-mark .brand-name { color: var(--paper); font-size: 22px; }
  .quote {
    position: absolute; left: 255px; top: 165px; width: 265px;
    color: var(--paper); font-size: 18px; line-height: 1.3;
  }
  .quote-author {
    display: block; margin-top: 10px; color: var(--leaf);
    font-size: 15px; font-style: normal;
  }
</style>
</head>
<body>
<main class="stage">
  <section class="card card-front">
    <svg class="front-swoop" viewBox="0 0 540 330" aria-hidden="true">
      <path d="M0,304 C190,296 380,250 540,162" fill="none" stroke="var(--leaf)" stroke-width="4"/>
      <path d="M0,312 C190,304 380,262 540,176 L540,330 L0,330 Z" fill="var(--plum)"/>
    </svg>
    <div class="brand">
      <p class="brand-name">Tallowood<br>KinderMove</p>
      <span class="brand-dot"></span>
    </div>
    <div class="divider"></div>
    <div class="details">
      <h1 class="person-name">Mira Toveland</h1>
      <p class="credential">Occupational Therapist</p>
      <p class="credential">Child Centred Play Therapist</p>
      <p class="address">PO Box 71<br>Marrowbank WA 6401</p>
      <ul class="contact-list">
        <li><svg viewBox="0 0 10 10"><path d="M2,0 L4,2 L3,3.5 Q4.5,6 6.5,7 L8,6 L10,8 L8.5,10 Q3,9 0,2 Z"/></svg>0487 552 019</li>
        <li><svg viewBox="0 0 10 10"><path d="M0,2 H10 V8 H0 Z M0,2 L5,5.5 L10,2" stroke="#fff" stroke-width="0.8"/></svg>mira@tkmove.com.au</li>
        <li><svg viewBox="0 0 10 10"><circle cx="5" cy="5" r="5"/></svg>www.tkmove.com.au</li>
      </ul>
    </div>
  </section>

  <section class="card card-back">
    <div class="back-mark">
      <span class="brand-dot"></span>
      <p class="brand-name">Tallowood KinderMove</p>
    </div>
    <blockquote class="quote">
      "Play is a child's language and toys are their words"
      <cite class="quote-author">Delbert Quorin</cite>
    </blockquote>
  </section>
</main>
</body>
</html>
```